添付しますサイズで、添付する2つのロゴを配置し、空いたスペースに提携駐車場ありや車で通えることを訴える看板デザインとなります。文字のフォントや大きさ、色調や縁取りを作るかなど、ご提案いただければと存じます。

①横長ステンレス…右寄せでTevo GymとMorvaのロゴを配置
左スペースに『提携駐車場あります』の文言。もしくは文字バランスを見て、
文言の変更もお願い致します。

②縦長看板に上にMorva、その下につなげてTevo Gym、さらにその下に
『車で通える』もしくは『Pあり』などのご提案をお願い致します。

上記、セットなので、例えば横長の方に『車で通える』、縦長に『P有』なども
良いかもしれません。宜しくお願い致します。
ロゴを2つ並べて配置、提携駐車場があることと、車で通えることのアピール
青系、水色系、無彩色系
イメージが確定してご納品いただく際に、pngやaiの拡張子データが必要でしたら、その際にデータをお渡しさせていただきます。
道路からの見え方の参考としまして、住所:埼玉県さいたま市南区桜台3-8-21で検索していただくと、
白い建物が当店となります。

高級感のあるお店作りを目指しておりますので、看板で高級感を訴求したいです。
また、今後のぼりの制作も考えています。
お世話になります。現在までのご提案、誠にありがとうございます。
ステンレスの横長看板ですが、『前面シート被せ』となるとのことです。

また、色味についてですが、私の指定させていただいた『青』『緑』『黒』でなく、
上品で高級なイメージでいただけましたら色はこだわりません。

どうぞ宜しくお願い致します。

自分の考えを1番表現していただいたことが決め手です!

この度は多くのご提案をいただきまして、ありがとうございました。
皆様のデザインは素晴らしいものばかりでした。

心より御礼申し上げます。

```html
<!DOCTYPE html>
<html lang="ja">
<head>
<meta charset="utf-8">
<title>Tevo Gym / Morva 看板デザイン</title>
<link rel="stylesheet" href="https://fonts.googleapis.com/css2?family=Cormorant+Garamond:wght@500&family=Noto+Sans+JP:wght@500;700&display=swap">
<style>
:root{
  --teal:#1ba3a6;
  --teal-dark:#12898c;
  --ink:#5e6466;
  --board:#ffffff;
  --edge:#d5d8d9;
  --steel-a:#f4f5f5;
  --steel-b:#c9cccd;
  --bg:#ffffff;
}
*{margin:0;padding:0;box-sizing:border-box}
html,body{width:874px;height:1200px;overflow:hidden;background:var(--bg)}
.canvas{position:relative;width:874px;height:1200px;font-family:"Noto Sans JP",sans-serif}
.sign{position:absolute;border:1px solid var(--edge);background:var(--board)}
.sign-wide{left:117px;width:611px;height:148px}
.sign-white{top:35px;box-shadow:0 0 0 8px #f1f2f2}
.sign-steel{top:210px;background:linear-gradient(180deg,var(--steel-b) 0%,var(--steel-a) 45%,var(--steel-b) 100%);box-shadow:0 0 0 8px #eceeee}
.sign-tall{top:402px;width:285px;height:743px;box-shadow:0 0 0 6px #f3f4f4}
.sign-tall.left{left:117px}
.sign-tall.right{left:440px}
.post{position:absolute;left:787px;top:402px;width:20px;height:743px;background:var(--teal)}

.parking{position:absolute;display:flex;align-items:flex-end;color:var(--teal);font-weight:700;line-height:1}
.parking .p{font-family:"Noto Sans JP",sans-serif}
.parking .has{color:var(--teal-dark)}
.sign-wide .parking{left:22px;top:34px}
.sign-wide .parking .p{font-size:76px}
.sign-wide .parking .has{font-size:34px;margin-left:4px;margin-bottom:6px}
.sign-steel .parking{color:var(--teal-dark)}

.name{font-family:"Cormorant Garamond",serif;font-weight:500;color:var(--ink);text-align:center;line-height:1}
.mark{display:block;margin:0 auto;border-radius:50%;background:var(--teal)}
.sub{font-family:"Cormorant Garamond",serif;color:var(--ink);text-align:center;letter-spacing:.2em}

.wide-logos{position:absolute;right:70px;top:26px;display:flex;gap:40px;align-items:flex-end}
.wide-logos .logo{width:120px}
.wide-logos .mark{width:26px;height:26px;margin-bottom:8px}
.wide-logos .name{font-size:30px}
.wide-logos .sub{font-size:9px;margin-top:4px;letter-spacing:.1em}

.tall-logo{position:absolute;left:0;width:100%}
.tall-logo.morva{top:36px}
.tall-logo.tevo{top:245px}
.tall-logo .mark{width:58px;height:58px;margin-bottom:16px}
.tall-logo .name{font-size:58px}
.tall-logo .sub{font-size:14px;margin-top:10px;letter-spacing:.05em}
.tall-logo.tevo .sub{font-size:18px;letter-spacing:.35em}

.car{position:absolute;left:40px;top:488px;width:205px;height:140px;border-radius:22px;background:linear-gradient(180deg,#e3f3f3,#c9e9e9)}
.drive-text{position:absolute;left:0;width:100%;top:685px;text-align:center;color:var(--teal);font-size:30px;font-weight:700}
.sign-tall .parking{left:50px;top:500px}
.sign-tall .parking .p{font-size:190px}
.sign-tall .parking .has{font-size:70px;margin-left:6px;margin-bottom:16px}
</style>
</head>
<body>
<div class="canvas">

  <section class="sign sign-wide sign-white">
    <div class="parking"><span class="p">P</span><span class="has">有</span></div>
    <div class="wide-logos">
      <div class="logo"><span class="mark"></span><div class="name">Tevo Gym</div><div class="sub">PRIVATE</div></div>
      <div class="logo"><span class="mark"></span><div class="name">Morva</div><div class="sub">body conditioning &amp; healing salon</div></div>
    </div>
  </section>

  <section class="sign sign-wide sign-steel">
    <div class="parking"><span class="p">P</span><span class="has">有</span></div>
    <div class="wide-logos">
      <div class="logo"><span class="mark"></span><div class="name">Tevo Gym</div><div class="sub">PRIVATE</div></div>
      <div class="logo"><span class="mark"></span><div class="name">Morva</div><div class="sub">body conditioning &amp; healing salon</div></div>
    </div>
  </section>

  <section class="sign sign-tall left">
    <div class="tall-logo morva"><span class="mark"></span><div class="name">Morva</div><div class="sub">body conditioning &amp; healing salon</div></div>
    <div class="tall-logo tevo"><span class="mark"></span><div class="name">Tevo Gym</div><div class="sub">PRIVATE</div></div>
    <div class="car" role="img" aria-label="車のアイコン"></div>
    <p class="drive-text">お車で通えます</p>
  </section>

  <section class="sign sign-tall right">
    <div class="tall-logo morva"><span class="mark"></span><div class="name">Morva</div><div class="sub">body conditioning &amp; healing salon</div></div>
    <div class="tall-logo tevo"><span class="mark"></span><div class="name">Tevo Gym</div><div class="sub">PRIVATE</div></div>
    <div class="parking"><span class="p">P</span><span class="has">有</span></div>
  </section>

  <div class="post"></div>
</div>
</body>
</html>
```